Recipe Card Design

I have a small kitchen store in Livingston Montana, and I would like to have recipe cards (4x6 postcard) designed with my logo, lines for recipe writing, all in black and white. My website is here: www.copperladlehouse.com

Store

```html
<!DOCTYPE html>
<html lang="en">
<head>
<meta charset="utf-8">
<title>Copper Ladle House – Recipe Card Back</title>
<link rel="stylesheet" href="https://fonts.googleapis.com/css2?family=Source+Sans+3:wght@300;400;600&display=swap">
<style>
  :root {
    --paper: #ffffff;
    --ink-soft: #8a8a8a;
    --ink-mid: #5e5e5e;
    --rule: #9a9a9a;
    --mark: #8c8c8c;
  }
  html, body {
    margin: 0;
    padding: 0;
    width: 1200px;
    height: 930px;
    overflow: hidden;
    background: var(--paper);
  }
  .card {
    position: relative;
    width: 1200px;
    height: 930px;
    background: var(--paper);
    font-family: "Source Sans 3", "Source Sans Pro", sans-serif;
  }
  .brand-mark {
    position: absolute;
    left: 66px;
    top: 52px;
    width: 200px;
    height: 250px;
    display: flex;
    flex-direction: column;
    align-items: flex-start;
    gap: 16px;
  }
  .brand-mark__square {
    width: 40px;
    height: 40px;
    background: var(--mark);
  }
  .brand-mark__name {
    margin: 0;
    font-weight: 600;
    font-size: 36px;
    line-height: 1.05;
    color: var(--mark);
    text-transform: uppercase;
    letter-spacing: 0.02em;
  }
  .store-info {
    position: absolute;
    left: 297px;
    top: 54px;
    margin: 0;
    font-style: normal;
    font-weight: 300;
    font-size: 23px;
    line-height: 29px;
    color: var(--ink-soft);
  }
  .store-info__name {
    display: block;
    font-size: 24px;
    text-transform: uppercase;
  }
  .stamp-box {
    position: absolute;
    left: 965px;
    top: 51px;
    width: 189px;
    height: 225px;
    border: 1px solid var(--rule);
    box-sizing: border-box;
  }
  .divider {
    position: absolute;
    left: 693px;
    top: 277px;
    width: 1px;
    height: 603px;
    background: var(--rule);
  }
  .website {
    position: absolute;
    left: 214px;
    top: 857px;
    margin: 0;
    font-weight: 400;
    font-size: 23px;
    line-height: 30px;
    color: var(--ink-mid);
  }
</style>
</head>
<body>
  <main class="card">
    <div class="brand-mark">
      <span class="brand-mark__square" aria-hidden="true"></span>
      <p class="brand-mark__name">Copper Ladle House</p>
    </div>

    <address class="store-info">
      <span class="store-info__name">Copper Ladle House</span>
      218 West Park Lane, Cedar Hollow,<br>
      WY 82414<br>
      (307) 555-0148
    </address>

    <div class="stamp-box" aria-label="Stamp area"></div>
    <div class="divider" aria-hidden="true"></div>

    <p class="website">copperladlehouse.com</p>
  </main>
</body>
</html>
```